PELDRAX Business Cards

We require a business card for our company that provides IT consulting services. We already have a logo that needs to be used on the card. We want a clean professional looking design that incorporates our colours. Our main focus is providing managed services to business, which involves us looking after all of their IT requirements including managing servers/networks, projects, and procurement.

Industry/Entity Type

Information Technology

Requirements
Must have
• our logo, contact information, name, title, phone numbers

```html
<!DOCTYPE html>
<html lang="en">
<head>
<meta charset="utf-8">
<title>PELDRAX Business Card</title>
<link href="https://fonts.googleapis.com/css2?family=Poppins:wght@400;500;600&display=swap" rel="stylesheet">
<style>
  :root {
    --brand-blue: #1a9ad8;
    --card-white: #ffffff;
    --ink: #1c1c1e;
    --ink-soft: #2e2e30;
    --card-black: #141416;
    --stage: #e4e6e9;
  }
  * { margin: 0; padding: 0; box-sizing: border-box; }
  html, body { width: 1200px; height: 900px; overflow: hidden; }
  body {
    background: var(--stage);
    font-family: "Poppins", sans-serif;
    display: flex;
    align-items: center;
    justify-content: center;
    gap: 60px;
  }
  .card {
    position: relative;
    width: 520px;
    height: 300px;
    border-radius: 22px;
    overflow: hidden;
    box-shadow: 0 14px 30px rgba(0,0,0,0.18);
  }
  .card-front { background: var(--card-white); }
  .card-back {
    background: var(--card-black);
    display: flex;
    align-items: center;
    justify-content: center;
  }

  .holder { position: absolute; left: 34px; top: 30px; }
  .holder-name {
    color: var(--brand-blue);
    font-weight: 500;
    font-size: 19px;
    letter-spacing: 0.5px;
    line-height: 1.1;
  }
  .holder-title { color: var(--ink); font-size: 13px; line-height: 1.2; }
  .divider {
    width: 14px; height: 2px;
    background: var(--brand-blue);
    margin: 14px 0 12px;
  }
  .address { color: var(--ink); font-size: 12px; line-height: 1.35; }
  .contact-list { list-style: none; margin-top: 10px; }
  .contact-item {
    display: flex; align-items: center; gap: 9px;
    color: var(--ink); font-size: 12.5px; line-height: 1.7;
  }
  .contact-icon { width: 13px; height: 13px; flex: none; }

  .front-wordmark {
    position: absolute;
    right: 44px; top: 82px;
    color: var(--brand-blue);
    font-weight: 600;
    font-size: 40px;
    letter-spacing: 3px;
  }

  .footer-band { position: absolute; left: 0; bottom: 0; width: 520px; height: 74px; }
  .website {
    position: absolute;
    right: 34px; bottom: 16px;
    color: var(--card-white);
    font-size: 17px;
    letter-spacing: 0.5px;
  }
  .website-accent { color: var(--brand-blue); }

  .back-wordmark {
    color: var(--brand-blue);
    font-weight: 600;
    font-size: 54px;
    letter-spacing: 6px;
  }
</style>
</head>
<body>

  <section class="card card-front" aria-label="Business card front">
    <div class="holder">
      <p class="holder-name">MARLON TEAGUE</p>
      <p class="holder-title">owner</p>
      <div class="divider"></div>
      <p class="address">48 Harbor Lane<br>Box 902, Elm Ridge, AB</p>
      <ul class="contact-list">
        <li class="contact-item">
          <svg class="contact-icon" viewBox="0 0 16 16" aria-hidden="true">
            <rect width="16" height="16" rx="3" fill="#1a9ad8"/>
            <path d="M5 3.5c.5 0 1 .9 1.3 1.8.2.6-.6 1-.6 1.4.2 1.2 1.5 2.6 2.8 3 .4 0 .8-.8 1.4-.6.9.3 1.8.8 1.8 1.3 0 .8-1 1.6-1.9 1.6C6.6 12 4 9.4 4 5.4 4 4.5 4.5 3.5 5 3.5z" fill="#fff"/>
          </svg>
          403-555-0182
        </li>
        <li class="contact-item">
          <svg class="contact-icon" viewBox="0 0 16 16" aria-hidden="true">
            <rect y="2" width="16" height="12" rx="1.5" fill="#1a9ad8"/>
            <path d="M1.5 4l6.5 5 6.5-5" fill="none" stroke="#fff" stroke-width="1.4"/>
          </svg>
          email@peldrax.com
        </li>
      </ul>
    </div>

    <p class="front-wordmark">PELDRAX</p>

    <svg class="footer-band" viewBox="0 0 520 74" aria-hidden="true">
      <rect x="0" y="22" width="520" height="5" fill="#1a9ad8"/>
      <rect x="0" y="33" width="520" height="41" fill="#1a9ad8"/>
      <path d="M250 74 L250 50 Q250 36 264 36 L300 36 Q318 36 326 30 Q334 24 346 24 L520 24 L520 74 Z" fill="#1c1c1e"/>
    </svg>
    <p class="website">www.pel<span class="website-accent">drax</span>.com</p>
  </section>

  <section class="card card-back" aria-label="Business card back">
    <p class="back-wordmark">PELDRAX</p>
  </section>

</body>
</html>
```